Plantain chip snack pack bag design + company logo design

We need to design a bag for a new snack food company. The brand is called "Crunch Bloom," and the first product, plantain chips, will come in 4 flavors - Classic Unripe, Sweet 'n Spicy!!, Original Sweet, and Ginger & Soy. The bag - which we plan to print in multiple sizes - needs to have a clear section on the front so the contents are visible, as they will be sold by street vendors and ability to view the contents is key. Design needs to be "very happy and exciting" and feature simple, strong colors that say "delicious and crispy" i.e. Classic Unripe is green, Sweet 'n Spicy!! is red, Original Sweet is yellow, and Ginger & Soy is tan (plus these will be printed in mass so must be simple yet very catchy on shelves and on the street vendors). On the back, there needs to be a column of nutritional content, plus the company contact address, email, phone lines, Twitter/Facebook/Instagram handles, and the quality certification number. Also, on the back, a bar code and "Made in xxx" text. Finally, the net weight of contents needs to be on the front as well. I have uploaded a sample of a competing product's packaging as inspiration only (NOT TO BE COPIED but to our design MUST BE MORE CATCHY, ATTRACTIVE, and FUN than this one)

Target Market(s)

All snack consumers, especially those with a bias toward healthier eating.

Industry/Entity Type

It Company

Logo Text

Delight in every bite!

Font styles to use
Serif
Decorative
Script

Requirements
Must have
• 1. For the package design, handoffs must include placeholders for ALL text so we can edit the text as needed
• 2. For package design, large transparent section on bag is critical so contents are visible; also, branding of "Crunch Bloom" must be large and recognizable from a distance
• 3. Primary colors suitable for industrial mass production
• 4. Logo design on the bags must include the parent company name i.e. "Crunch Bloom Snacks by Tolvaro Foods"
• 5. Package must say "Plantain chips" and the flavor e.g. "Sweet 'n Spicy!!" and with a small image of a hot pepper (each flavor should have a similar small image representing the flavor)
• 6. For the Logo design portion of the project, the Tolvaro Foods Limited logo should incorporate plantains, coconuts, potatos and corn. This logo is for the parent company and Crunch Bloom is the plantain chip product line
Nice to have
• 1. Smiling faces suggesting happiness, health, friendliness, and overall delight at eating the chips

```html
<!DOCTYPE html>
<html lang="en">
<head>
<meta charset="utf-8">
<title>Crunch Bloom Plantain Chips – Flavour Range</title>
<link href="https://fonts.googleapis.com/css2?family=Fredoka:wght@600;700&family=Open+Sans:wght@400;600&display=swap" rel="stylesheet">
<style>
  :root{
    --backdrop-light:#ececec;
    --backdrop-dark:#c4c4c4;
    --brand-ink:#1f6b12;
    --outline:#1c1c1c;
    --chip-light:#ecd27a;
    --chip-dark:#c8973a;
  }
  html,body{margin:0;padding:0;overflow:hidden;}
  body{
    width:1200px;height:726px;position:relative;
    background:radial-gradient(ellipse at 50% 35%,var(--backdrop-light) 0%,var(--backdrop-dark) 100%);
    font-family:"Fredoka",sans-serif;
  }
  .pack{position:absolute;display:block;}
  .pack--large{width:245px;height:368px;top:62px;}
  .pack--small{width:122px;height:183px;top:498px;}
  .pack svg{width:100%;height:100%;display:block;}

  .flavour--unripe{--main:#3f9a1a;--accent:#93d62c;--title:#5fd02b;--badge:#7cc829;--icon:#3b7d16;}
  .flavour--sweet{--main:#d3cf22;--accent:#f6f25a;--title:#fff03a;--badge:#f3ea2e;--icon:#e9b93a;}
  .flavour--spicy{--main:#a3121a;--accent:#d3262a;--title:#e0201c;--badge:#d92822;--icon:#b3161a;}
  .flavour--ginger{--main:#7a4a14;--accent:#b8782a;--title:#f29a1d;--badge:#e99320;--icon:#b98a55;}

  .pack__body{fill:var(--main);}
  .pack__stripe{fill:var(--accent);opacity:.55;}
  .pack__window{fill:url(#chip-window);}
  .pack__swoosh{fill:var(--accent);}
  .pack__swoosh-edge{fill:none;stroke:#f2e24a;stroke-width:3;}
  .brand-name{font-family:"Fredoka",sans-serif;font-weight:700;font-size:30px;fill:var(--brand-ink);text-anchor:middle;}
  .brand-dot{fill:var(--brand-ink);}
  .brand-line{font-family:"Open Sans",sans-serif;font-weight:600;font-size:7.4px;fill:#2a2a2a;text-anchor:middle;}
  .product-title{font-family:"Fredoka",sans-serif;font-weight:700;font-size:42px;fill:var(--title);
    stroke:var(--outline);stroke-width:5;stroke-linejoin:round;paint-order:stroke;text-anchor:middle;}
  .flavour-badge__disc{fill:var(--badge);stroke:var(--outline);stroke-width:2.5;}
  .flavour-badge__icon{fill:var(--icon);}
  .flavour-badge__text{font-family:"Fredoka",sans-serif;font-weight:700;font-size:8.5px;fill:var(--outline);letter-spacing:.6px;}
  .shared-defs{position:absolute;width:0;height:0;}
</style>
</head>
<body>

<svg class="shared-defs" aria-hidden="true">
  <defs>
    <linearGradient id="chip-window" x1="0" y1="0" x2="0.4" y2="1">
      <stop offset="0" stop-color="#ecd27a"/>
      <stop offset="0.55" stop-color="#ddb456"/>
      <stop offset="1" stop-color="#c8973a"/>
    </linearGradient>
    <path id="badge-arc-top" d="M-20 0 A20 20 0 0 1 20 0"/>
    <path id="badge-arc-bottom" d="M-27 0 A27 27 0 0 0 27 0"/>
  </defs>
</svg>

<!-- Large packs -->
<div class="pack pack--large flavour--unripe" style="left:45px">
  <svg viewBox="0 0 240 360">
    <rect class="pack__body" width="240" height="360"/>
    <path class="pack__stripe" d="M60 360 L100 300 L120 310 L95 360 Z M150 360 L170 290 L190 282 L185 360 Z"/>
    <path class="pack__window" role="img" aria-label="Transparent window showing golden plantain chips" d="M0 18 Q120 4 240 18 V250 Q140 300 0 330 Z"/>
    <path class="pack__swoosh" d="M0 330 Q140 300 240 250 V270 Q150 318 0 346 Z"/>
    <path class="pack__swoosh-edge" d="M0 330 Q140 300 240 250"/>
    <text class="brand-name" x="110" y="56">Crunch</text>
    <text class="brand-name" x="110" y="86">Bloom</text>
    <circle class="brand-dot" cx="196" cy="44" r="8"/>
    <text class="brand-line" x="120" y="102">Crunch Bloom Snacks by Tolvaro Foods</text>
    <g transform="rotate(-4 120 170)">
      <text class="product-title" x="120" y="152">Plantain</text>
      <text class="product-title" x="112" y="192">Chips</text>
    </g>
    <g class="flavour-badge" transform="translate(192 262) rotate(-20)">
      <circle class="flavour-badge__disc" r="31"/>
      <circle class="flavour-badge__icon" r="12" role="img" aria-label="Small drawing of green unripe plantains"/>
      <text class="flavour-badge__text" text-anchor="middle"><textPath href="#badge-arc-top" startOffset="50%">CLASSIC</textPath></text>
      <text class="flavour-badge__text" text-anchor="middle"><textPath href="#badge-arc-bottom" startOffset="50%">UNRIPE</textPath></text>
    </g>
  </svg>
</div>

<div class="pack pack--large flavour--sweet" style="left:325px">
  <svg viewBox="0 0 240 360">
    <rect class="pack__body" width="240" height="360"/>
    <path class="pack__stripe" d="M60 360 L100 300 L120 310 L95 360 Z M150 360 L170 290 L190 282 L185 360 Z"/>
    <path class="pack__window" role="img" aria-label="Transparent window showing golden plantain chips" d="M0 18 Q120 4 240 18 V250 Q140 300 0 330 Z"/>
    <path class="pack__swoosh" d="M0 330 Q140 300 240 250 V270 Q150 318 0 346 Z"/>
    <path class="pack__swoosh-edge" d="M0 330 Q140 300 240 250"/>
    <text class="brand-name" x="110" y="56">Crunch</text>
    <text class="brand-name" x="110" y="86">Bloom</text>
    <circle class="brand-dot" cx="196" cy="44" r="8"/>
    <text class="brand-line" x="120" y="102">Crunch Bloom Snacks by Tolvaro Foods</text>
    <g transform="rotate(-4 120 170)">
      <text class="product-title" x="120" y="152">Plantain</text>
      <text class="product-title" x="112" y="192">Chips</text>
    </g>
    <g class="flavour-badge" transform="translate(192 262) rotate(-20)">
      <circle class="flavour-badge__disc" r="31"/>
      <circle class="flavour-badge__icon" r="12" role="img" aria-label="Small drawing of ripe plantain slices"/>
      <text class="flavour-badge__text" text-anchor="middle"><textPath href="#badge-arc-top" startOffset="50%">ORIGINAL</textPath></text>
      <text class="flavour-badge__text" text-anchor="middle"><textPath href="#badge-arc-bottom" startOffset="50%">SWEET</textPath></text>
    </g>
  </svg>
</div>

<div class="pack pack--large flavour--spicy" style="left:610px">
  <svg viewBox="0 0 240 360">
    <rect class="pack__body" width="240" height="360"/>
    <path class="pack__stripe" d="M60 360 L100 300 L120 310 L95 360 Z M150 360 L170 290 L190 282 L185 360 Z"/>
    <path class="pack__window" role="img" aria-label="Transparent window showing golden plantain chips" d="M0 18 Q120 4 240 18 V250 Q140 300 0 330 Z"/>
    <path class="pack__swoosh" d="M0 330 Q140 300 240 250 V270 Q150 318 0 346 Z"/>
    <path class="pack__swoosh-edge" d="M0 330 Q140 300 240 250"/>
    <text class="brand-name" x="110" y="56">Crunch</text>
    <text class="brand-name" x="110" y="86">Bloom</text>
    <circle class="brand-dot" cx="196" cy="44" r="8"/>
    <text class="brand-line" x="120" y="102">Crunch Bloom Snacks by Tolvaro Foods</text>
    <g transform="rotate(-4 120 170)">
      <text class="product-title" x="120" y="152">Plantain</text>
      <text class="product-title" x="112" y="192">Chips</text>
    </g>
    <g class="flavour-badge" transform="translate(192 262) rotate(-20)">
      <circle class="flavour-badge__disc" r="31"/>
      <circle class="flavour-badge__icon" r="12" role="img" aria-label="Small drawing of red hot peppers"/>
      <text class="flavour-badge__text" text-anchor="middle"><textPath href="#badge-arc-top" startOffset="50%">SWEET</textPath></text>
      <text class="flavour-badge__text" text-anchor="middle"><textPath href="#badge-arc-bottom" startOffset="50%">N' SPICY</textPath></text>
    </g>
  </svg>
</div>

<div class="pack pack--large flavour--ginger" style="left:895px">
  <svg viewBox="0 0 240 360">
    <rect class="pack__body" width="240" height="360"/>
    <path class="pack__stripe" d="M60 360 L100 300 L120 310 L95 360 Z M150 360 L170 290 L190 282 L185 360 Z"/>
    <path class="pack__window" role="img" aria-label="Transparent window showing golden plantain chips" d="M0 18 Q120 4 240 18 V250 Q140 300 0 330 Z"/>
    <path class="pack__swoosh" d="M0 330 Q140 300 240 250 V270 Q150 318 0 346 Z"/>
    <path class="pack__swoosh-edge" d="M0 330 Q140 300 240 250"/>
    <text class="brand-name" x="110" y="56">Crunch</text>
    <text class="brand-name" x="110" y="86">Bloom</text>
    <circle class="brand-dot" cx="196" cy="44" r="8"/>
    <text class="brand-line" x="120" y="102">Crunch Bloom Snacks by Tolvaro Foods</text>
    <g transform="rotate(-4 120 170)">
      <text class="product-title" x="120" y="152">Plantain</text>
      <text class="product-title" x="112" y="192">Chips</text>
    </g>
    <g class="flavour-badge" transform="translate(192 262) rotate(-20)">
      <circle class="flavour-badge__disc" r="31"/>
      <circle class="flavour-badge__icon" r="12" role="img" aria-label="Small drawing of ginger root"/>
      <text class="flavour-badge__text" text-anchor="middle"><textPath href="#badge-arc-top" startOffset="50%">GINGER</textPath></text>
      <text class="flavour-badge__text" text-anchor="middle"><textPath href="#badge-arc-bottom" startOffset="50%">AND SOY</textPath></text>
    </g>
  </svg>
</div>

<!-- Flat artwork panels -->
<div class="pack pack--small flavour--unripe" style="left:578px">
  <svg viewBox="0 0 240 360">
    <rect class="pack__body" width="240" height="360"/>
    <path class="pack__window" role="img" aria-label="Plantain chips window" d="M0 18 Q120 4 240 18 V250 Q140 300 0 330 Z"/>
    <path class="pack__swoosh" d="M0 330 Q140 300 240 250 V270 Q150 318 0 346 Z"/>
    <text class="brand-name" x="110" y="56">Crunch</text>
    <text class="brand-name" x="110" y="86">Bloom</text>
    <circle class="brand-dot" cx="196" cy="44" r="8"/>
    <text class="brand-line" x="120" y="102">Crunch Bloom Snacks by Tolvaro Foods</text>
    <g transform="rotate(-4 120 170)">
      <text class="product-title" x="120" y="152">Plantain</text>
      <text class="product-title" x="112" y="192">Chips</text>
    </g>
    <g transform="translate(192 262) rotate(-20)">
      <circle class="flavour-badge__disc" r="31"/>
      <circle class="flavour-badge__icon" r="12" role="img" aria-label="Unripe plantains"/>
      <text class="flavour-badge__text" text-anchor="middle"><textPath href="#badge-arc-top" startOffset="50%">CLASSIC</textPath></text>
      <text class="flavour-badge__text" text-anchor="middle"><textPath href="#badge-arc-bottom" startOffset="50%">UNRIPE</textPath></text>
    </g>
  </svg>
</div>

<div class="pack pack--small flavour--sweet" style="left:718px">
  <svg viewBox="0 0 240 360">
    <rect class="pack__body" width="240" height="360"/>
    <path class="pack__window" role="img" aria-label="Plantain chips window" d="M0 18 Q120 4 240 18 V250 Q140 300 0 330 Z"/>
    <path class="pack__swoosh" d="M0 330 Q140 300 240 250 V270 Q150 318 0 346 Z"/>
    <text class="brand-name" x="110" y="56">Crunch</text>
    <text class="brand-name" x="110" y="86">Bloom</text>
    <circle class="brand-dot" cx="196" cy="44" r="8"/>
    <text class="brand-line" x="120" y="102">Crunch Bloom Snacks by Tolvaro Foods</text>
    <g transform="rotate(-4 120 170)">
      <text class="product-title" x="120" y="152">Plantain</text>
      <text class="product-title" x="112" y="192">Chips</text>
    </g>
    <g transform="translate(192 262) rotate(-20)">
      <circle class="flavour-badge__disc" r="31"/>
      <circle class="flavour-badge__icon" r="12" role="img" aria-label="Ripe plantain slices"/>
      <text class="flavour-badge__text" text-anchor="middle"><textPath href="#badge-arc-top" startOffset="50%">ORIGINAL</textPath></text>
      <text class="flavour-badge__text" text-anchor="middle"><textPath href="#badge-arc-bottom" startOffset="50%">SWEET</textPath></text>
    </g>
  </svg>
</div>

<div class="pack pack--small flavour--spicy" style="left:857px">
  <svg viewBox="0 0 240 360">
    <rect class="pack__body" width="240" height="360"/>
    <path class="pack__window" role="img" aria-label="Plantain chips window" d="M0 18 Q120 4 240 18 V250 Q140 300 0 330 Z"/>
    <path class="pack__swoosh" d="M0 330 Q140 300 240 250 V270 Q150 318 0 346 Z"/>
    <text class="brand-name" x="110" y="56">Crunch</text>
    <text class="brand-name" x="110" y="86">Bloom</text>
    <circle class="brand-dot" cx="196" cy="44" r="8"/>
    <text class="brand-line" x="120" y="102">Crunch Bloom Snacks by Tolvaro Foods</text>
    <g transform="rotate(-4 120 170)">
      <text class="product-title" x="120" y="152">Plantain</text>
      <text class="product-title" x="112" y="192">Chips</text>
    </g>
    <g transform="translate(192 262) rotate(-20)">
      <circle class="flavour-badge__disc" r="31"/>
      <circle class="flavour-badge__icon" r="12" role="img" aria-label="Red hot peppers"/>
      <text class="flavour-badge__text" text-anchor="middle"><textPath href="#badge-arc-top" startOffset="50%">SWEET</textPath></text>
      <text class="flavour-badge__text" text-anchor="middle"><textPath href="#badge-arc-bottom" startOffset="50%">N' SPICY</textPath></text>
    </g>
  </svg>
</div>

<div class="pack pack--small flavour--ginger" style="left:996px">
  <svg viewBox="0 0 240 360">
    <rect class="pack__body" width="240" height="360"/>
    <path class="pack__window" role="img" aria-label="Plantain chips window" d="M0 18 Q120 4 240 18 V250 Q140 300 0 330 Z"/>
    <path class="pack__swoosh" d="M0 330 Q140 300 240 250 V270 Q150 318 0 346 Z"/>
    <text class="brand-name" x="110" y="56">Crunch</text>
    <text class="brand-name" x="110" y="86">Bloom</text>
    <circle class="brand-dot" cx="196" cy="44" r="8"/>
    <text class="brand-line" x="120" y="102">Crunch Bloom Snacks by Tolvaro Foods</text>
    <g transform="rotate(-4 120 170)">
      <text class="product-title" x="120" y="152">Plantain</text>
      <text class="product-title" x="112" y="192">Chips</text>
    </g>
    <g transform="translate(192 262) rotate(-20)">
      <circle class="flavour-badge__disc" r="31"/>
      <circle class="flavour-badge__icon" r="12" role="img" aria-label="Ginger root"/>
      <text class="flavour-badge__text" text-anchor="middle"><textPath href="#badge-arc-top" startOffset="50%">GINGER</textPath></text>
      <text class="flavour-badge__text" text-anchor="middle"><textPath href="#badge-arc-bottom" startOffset="50%">AND SOY</textPath></text>
    </g>
  </svg>
</div>

</body>
</html>
```